New Business Card Design Project

Make a kick ass business card for The Otter Tea Mug, using the designs. I also might like the 2nd place design logo on the back? Maybe all black with that? Not sure. Also, I'm cool with it being on metal, plastic, glass? or whatever for the business card. Maybe shaped like a shark? Let me know what else you need? Would like designs in the next day or so. Thank you.
Target Market(s)
Anyone that is cool
Contact Information for Business Card
Name: Dorian Fenwick
Phone: 317.594.8126
inventor/creator/entrepreneur/owner
www.theottertyeamug.example
social media links
https://www.facebook.com/theottertyeamug
https://twitter.com/otter_brew
https://www.instagram.com/theottertyeamug/
I'll get the Pinterest one soon
Colors
Designer to choose colors to be used in the design.
Requirements
Must have
- The Otter Tea Mug
- www.theottertyeamug.example
- social media tags?
- My logos and picture/photo of wine glass
Nice to have
- Maybe shaped like a wine glass or shark
- I'll let you decide but my same colors from my website would be nice

```html
<!DOCTYPE html>
<html lang="en">
<head>
<meta charset="utf-8">
<title>Otter Tea Mug – Business Card</title>
<link rel="stylesheet" href="https://fonts.googleapis.com/css2?family=Noto+Serif:wght@400;700&family=Quicksand:wght@400&display=swap">
<style>
  :root {
    --backdrop: #2e2c2d;
    --paper: #ebebea;
    --paper-shade: #dcdcdb;
    --ink-dark: #1f1e1f;
    --ink-text: #2b2b2b;
    --brand-grey: #707070;
    --brand-red: #c04442;
    --white: #f4f4f4;
    --glass-tone: #d9d9d9;
  }
  * { margin: 0; padding: 0; box-sizing: border-box; }
  html, body {
    width: 1200px; height: 1200px; overflow: hidden;
    background: var(--backdrop);
  }
  .stage { position: relative; width: 1200px; height: 1200px; }

  .card {
    position: absolute; top: 446px;
    width: 540px; height: 308px;
    overflow: hidden;
  }
  .card--front { left: 48px; }
  .card--back { left: 612px; background: var(--paper); }

  /* front */
  .front-light {
    position: absolute; left: 0; top: 0; width: 50.3%; height: 100%;
    background: linear-gradient(90deg, var(--paper) 0%, var(--paper) 80%, var(--paper-shade) 100%);
  }
  .front-dark {
    position: absolute; right: 0; top: 0; width: 49.7%; height: 100%;
    background: var(--ink-dark);
  }
  .accent-bar {
    position: absolute; left: 263px; top: 61px;
    width: 17px; height: 186px; border-radius: 9px;
    background: var(--brand-red);
  }
  .wordmark {
    font-family: "Quicksand", sans-serif; font-weight: 400;
    color: var(--brand-grey); white-space: nowrap;
  }
  .front-light .wordmark {
    position: absolute; left: 0; width: 272px; top: 80px;
    text-align: center; font-size: 19px;
  }
  .social-list {
    position: absolute; left: 20px; top: 196px;
    list-style: none;
    font-family: "Noto Serif", serif; font-size: 14px; color: var(--ink-text);
  }
  .social-list li { display: flex; align-items: center; height: 25px; }
  .social-dot {
    width: 11px; height: 11px; border-radius: 50%;
    background: var(--brand-red); margin-right: 11px; flex: none;
  }

  .contact {
    position: absolute; right: 20px; top: 22px; text-align: right;
    font-family: "Noto Serif", serif; color: var(--white);
  }
  .contact-name { font-size: 21px; font-weight: 400; line-height: 1.1; }
  .contact-name strong { font-weight: 700; }
  .contact-role { font-size: 9px; margin-top: 4px; }
  .contact-phone { font-size: 17px; letter-spacing: 1.5px; margin-top: 6px; }

  .glass-art {
    position: absolute; left: 353px; top: 138px; width: 88px; height: 170px;
    background: linear-gradient(180deg, rgba(217,217,217,0.25) 0%, rgba(217,217,217,0.12) 100%);
    border-radius: 10px 10px 0 0;
  }
  .website {
    position: absolute; left: 270px; right: 0; top: 269px;
    text-align: center;
    font-family: "Noto Serif", serif; font-size: 9.5px; letter-spacing: 2px;
    color: var(--white);
  }

  /* back */
  .card--back .wordmark {
    position: absolute; left: 0; right: 0; top: 166px;
    text-align: center; font-size: 27px;
  }
</style>
</head>
<body>
<main class="stage">
  <section class="card card--front" aria-label="Business card front">
    <div class="front-light">
      <div class="wordmark">OtterTeaMug</div>
      <ul class="social-list">
        <li><span class="social-dot"></span>theottertyeamug</li>
        <li><span class="social-dot"></span>otter_brew</li>
        <li><span class="social-dot"></span>theottertyeamug</li>
        <li><span class="social-dot"></span>theottertyeamug</li>
      </ul>
    </div>
    <div class="front-dark">
      <div class="contact">
        <div class="contact-name"><strong>Dorian</strong> Fenwick</div>
        <div class="contact-role">inventor | creator | entrepreneur | owner</div>
        <div class="contact-phone">317.594.8126</div>
      </div>
    </div>
    <div class="glass-art" role="img" aria-label="Line drawing of a wine glass with the brand mark inside the bowl"></div>
    <div class="website">www.theottertyeamug.example</div>
    <div class="accent-bar"></div>
  </section>

  <section class="card card--back" aria-label="Business card back">
    <div class="wordmark">OtterTeaMug</div>
  </section>
</main>
</body>
</html>
```